Zenvok - Property Management Company Listings - PSD / uncoded only

Our site simply connects property owners with property managers. I’m asking you to create 2 pages, 1 homepage and 1 page that lists of property management companies. Build with Responsive Design in mind. PSD/uncoded files only. Help us create a great site!
Example competitor sites:
http://www.everyleaseguildhall.example/
http://www.tendourestates.example/
Inspired by these sites:
http://www.quorvix.example/
http://www.bespokuna.example/
http://www.fundlo.example/
https://www.tripnook.example/
I've attached the logo as well as 2 picture files that you can consider using.
• Zenvok Logo Colors: Yellow: HTML code: #FBC30A, RGB code: R: 251 G: 195 B: 10 Grey: HTML code: #4E4C4D, RGB code: R: 78 G: 76 B: 77
• The picture files are optional.
o One picture is of houses and neighborhood.
o The other is of a professional woman on the phone. Please do not use the professional woman as a large primary image. You can use the professional woman photo as a smaller photo and not the main photo.
• Please bring your own pictures and graphics too. Don't feel like you need to use mine.
Thank you!
Property Management

```html
<!DOCTYPE html>
<html lang="en">
<head>
<meta charset="utf-8">
<title>Zenvok – Find Your Local Property Manager</title>
<link href="https://fonts.googleapis.com/css2?family=Lato:wght@400;700&display=swap" rel="stylesheet">
<style>
  :root {
    --yellow: #fbc30a;
    --panel-yellow: rgba(244, 196, 10, 0.93);
    --grey: #4e4c4d;
    --dark-olive: #4d4428;
    --field: #fdf8e4;
    --card-bg: #f0f0f0;
    --text: #4e4c4d;
    --white: #ffffff;
  }
  * { box-sizing: border-box; margin: 0; padding: 0; }
  html, body { width: 1200px; height: 1156px; overflow: hidden; }
  body {
    position: relative;
    font-family: "Lato", sans-serif;
    color: var(--text);
    background: var(--white);
  }

  /* Header */
  .site-header { position: absolute; left: 0; top: 0; width: 1200px; height: 111px; background: var(--white); }
  .brand { position: absolute; left: 36px; top: 30px; display: flex; align-items: center; gap: 10px; }
  .brand-mark { width: 22px; height: 22px; background: var(--yellow); }
  .brand-name { font-size: 52px; font-weight: 700; color: var(--grey); line-height: 1; }
  .topline { position: absolute; right: 33px; top: 5px; font-size: 14px; display: flex; align-items: center; gap: 12px; color: var(--grey); }
  .main-nav { position: absolute; top: 55px; right: 0; display: flex; }
  .nav-item { position: absolute; transform: translateX(-50%); text-align: center; font-size: 17px; font-weight: 700; color: var(--grey); white-space: nowrap; }
  .nav-item svg { display: block; margin: 0 auto 5px; }

  /* Hero */
  .hero { position: absolute; left: 0; top: 111px; width: 1200px; height: 400px; }
  .hero-photo {
    position: absolute; inset: 0;
    background: linear-gradient(160deg, #5f6a55 0%, #7a7d6a 30%, #4d5a40 55%, #6b6a5c 75%, #3f4a35 100%);
  }
  .finder { position: absolute; left: 704px; top: 22px; width: 441px; height: 346px; background: var(--panel-yellow); }
  .finder-title { position: absolute; top: 29px; width: 100%; padding-left: 0; text-align: center; font-size: 17px; font-weight: 700; color: var(--grey); left: 0; text-indent: 0; }
  .finder-label { position: absolute; left: 29px; font-size: 15px; color: var(--grey); }
  .select-box { position: absolute; left: 28px; top: 100px; width: 349px; height: 36px; background: var(--field); }
  .select-btn { position: absolute; left: 377px; top: 100px; width: 36px; height: 36px; background: var(--dark-olive); display: flex; align-items: center; justify-content: center; }
  .zip-box { position: absolute; left: 29px; top: 179px; width: 111px; height: 36px; background: var(--field); }
  .search-btn { position: absolute; left: 174px; top: 179px; width: 107px; height: 36px; border-radius: 3px; background: var(--dark-olive); color: var(--white); font-size: 15px; display: flex; align-items: center; justify-content: center; gap: 14px; }
  .finder-note { position: absolute; left: 60px; top: 254px; width: 348px; text-align: center; font-size: 15px; line-height: 17px; color: var(--grey); }

  /* Steps */
  .section-title { position: absolute; top: 538px; left: 0; width: 1212px; text-align: center; font-size: 22px; font-weight: 700; color: var(--grey); }
  .step { position: absolute; top: 595px; width: 340px; height: 200px; background: var(--card-bg); border: 2px solid var(--yellow); text-align: center; }
  .step svg { position: absolute; top: 32px; left: 50%; transform: translateX(-50%); }
  .step-text { position: absolute; top: 126px; left: 6px; right: 6px; font-size: 17px; line-height: 17px; }

  /* Info boxes */
  .info { position: absolute; top: 837px; width: 528px; height: 221px; background: var(--card-bg); border: 2px solid var(--yellow); }
  .info-title { margin-top: 22px; text-align: center; font-size: 27px; font-weight: 400; color: var(--grey); }
  .reasons { list-style: none; margin-top: 22px; }
  .reasons li { position: relative; padding-left: 57px; font-size: 15px; height: 44px; }
  .reasons svg { position: absolute; left: 23px; top: 1px; }
  .pitch { margin: 22px 20px 0 20px; font-size: 15px; line-height: 26px; }
  .learn-btn { position: absolute; left: 179px; top: 150px; width: 154px; height: 48px; background: var(--grey); color: var(--white); font-size: 22px; display: flex; align-items: center; justify-content: center; border-radius: 2px; }

  /* Footer */
  .site-footer { position: absolute; left: 0; top: 1100px; width: 1200px; height: 56px; background: var(--grey); color: var(--white); font-size: 14px; }
  .copyright { position: absolute; left: 27px; top: 19px; }
  .footer-links { position: absolute; right: 21px; top: 19px; }
  .footer-links span.sep { margin: 0 5px; }
</style>
</head>
<body>

<header class="site-header">
  <div class="brand">
    <span class="brand-name">Zenvok</span>
    <span class="brand-mark"></span>
  </div>
  <div class="topline">
    <span>TALK TO EXPERT</span>
    <svg width="12" height="14" viewBox="0 0 12 14"><circle cx="6" cy="3.5" r="3.3" fill="#4e4c4d"/><path d="M0 14 Q0 7 6 7 Q12 7 12 14Z" fill="#4e4c4d"/></svg>
    <span>555-014-2290</span>
  </div>
  <nav class="main-nav">
    <a class="nav-item" style="left:-482px">
      <svg width="20" height="16" viewBox="0 0 20 16"><path d="M10 1 L1 8.5 L3 8.5 L3 16 L8 16 L8 11 L12 11 L12 16 L17 16 L17 8.5 L19 8.5Z" fill="#4e4c4d"/></svg>Home</a>
    <a class="nav-item" style="left:-289px">
      <svg width="14" height="18" viewBox="0 0 14 18"><circle cx="7" cy="6" r="5" fill="none" stroke="#4e4c4d" stroke-width="1.8"/><rect x="4.5" y="12" width="5" height="4" fill="#4e4c4d"/></svg>Are you a Property Manager?</a>
    <a class="nav-item" style="left:-77px">
      <svg width="18" height="18" viewBox="0 0 18 18"><rect width="18" height="18" rx="3" fill="#4e4c4d"/><path d="M5 4 L7.5 4 L8.5 7 L7 8 Q8 10.5 10 11 L11 9.5 L14 10.5 L14 13 Q8 14 5 7Z" fill="#fff"/></svg>Contact Us</a>
  </nav>
</header>

<section class="hero">
  <div class="hero-photo" role="img" aria-label="Aerial view of a suburban neighborhood with houses, driveways and trees"></div>
  <form class="finder">
    <h2 class="finder-title" style="padding-left:0;left:0;width:441px;transform:translateX(-1px)">FIND YOUR LOCAL PROPERTY MANAGER</h2>
    <label class="finder-label" style="top:76px">Select Your Property Type :</label>
    <div class="select-box"></div>
    <div class="select-btn">
      <svg width="12" height="12" viewBox="0 0 12 12"><path d="M2 1 L6 5 L10 1 M2 6 L6 10 L10 6" fill="none" stroke="#fff" stroke-width="1.8"/></svg>
    </div>
    <label class="finder-label" style="top:155px;left:28px">In Zipcode :</label>
    <div class="zip-box"></div>
    <div class="search-btn">
      <svg width="16" height="16" viewBox="0 0 16 16"><circle cx="6.5" cy="6.5" r="5" fill="none" stroke="#fff" stroke-width="2.4"/><path d="M10 10 L15 15" stroke="#fff" stroke-width="2.6"/></svg>
      <span>Search</span>
    </div>
    <p class="finder-note">Search our directory to find experienced and professional property management companies that meet your needs.</p>
  </form>
</section>

<h2 class="section-title">To Find Property Management Companies Near You</h2>

<div class="step" style="left:48px">
  <svg width="80" height="72" viewBox="0 0 80 72"><path d="M33 2 L2 30 L8 30 L8 54 L28 54 L28 40 L38 40 L38 54 L50 54 L50 30 L64 30 L52 19 L52 4 L45 4 L45 13Z" fill="#4e4c4d"/><rect x="48" y="40" width="28" height="26" rx="3" fill="none" stroke="#fbc30a" stroke-width="3"/><path d="M53 52 L60 59 L76 42" fill="none" stroke="#fbc30a" stroke-width="4"/></svg>
  <p class="step-text">Select your property type and zipcode</p>
</div>
<div class="step" style="left:429px">
  <svg width="84" height="72" viewBox="0 0 84 72"><rect x="2" y="2" width="72" height="56" rx="4" fill="#4e4c4d"/><rect x="7" y="13" width="62" height="40" fill="#f0f0f0"/><g fill="#4e4c4d"><rect x="10" y="19" width="4" height="4"/><rect x="17" y="19" width="46" height="4"/><rect x="10" y="27" width="4" height="4"/><rect x="17" y="27" width="46" height="4"/><rect x="10" y="35" width="4" height="4"/><rect x="17" y="35" width="46" height="4"/><rect x="10" y="43" width="4" height="4"/><rect x="17" y="43" width="40" height="4"/></g><circle cx="68" cy="49" r="7" fill="#fbc30a"/><path d="M54 71 Q54 57 68 57 Q82 57 82 71Z" fill="#fbc30a"/></svg>
  <p class="step-text" style="top:125px">Review property manager listings in your area</p>
</div>
<div class="step" style="left:810px">
  <svg width="76" height="72" viewBox="0 0 76 72"><path d="M2 0 L36 0 L50 14 L50 58 L2 58Z" fill="#4e4c4d"/><path d="M36 0 L36 14 L50 14" fill="#f0f0f0" opacity="0.6"/><g fill="#f0f0f0"><rect x="10" y="22" width="24" height="4"/><rect x="10" y="30" width="24" height="4"/><rect x="10" y="38" width="18" height="4"/></g><circle cx="48" cy="44" r="5" fill="#fbc30a"/><circle cx="66" cy="44" r="5" fill="#fbc30a"/><circle cx="57" cy="50" r="6" fill="#fbc30a"/><path d="M40 66 Q40 54 48 54 Q54 54 56 60 L58 60 Q60 54 66 54 Q74 54 74 66Z" fill="#fbc30a"/><path d="M46 70 Q46 58 57 58 Q68 58 68 70Z" fill="#fbc30a"/></svg>
  <p class="step-text">Select and compare property managers</p>
</div>

<section class="info" style="left:48px">
  <h3 class="info-title">What You have to choose Us?</h3>
  <ul class="reasons">
    <li><svg width="18" height="18" viewBox="0 0 18 18"><path d="M1 7 L10 7 L10 2 L17 9 L10 16 L10 11 L1 11Z" fill="#fbc30a"/></svg>Making renting Your home an easy, stress-free experience.</li>
    <li><svg width="18" height="18" viewBox="0 0 18 18"><path d="M1 7 L10 7 L10 2 L17 9 L10 16 L10 11 L1 11Z" fill="#fbc30a"/></svg>Connecting property owners with property managers.</li>
    <li><svg width="18" height="18" viewBox="0 0 18 18"><path d="M1 7 L10 7 L10 2 L17 9 L10 16 L10 11 L1 11Z" fill="#fbc30a"/></svg>Providing property management solutions, simplified.</li>
  </ul>
</section>

<section class="info" style="left:624px">
  <h3 class="info-title">Are you a Property Manager?</h3>
  <p class="pitch">Join our real estate property management company network. Let us help you find leads of property owners seeking to rent their homes.</p>
  <a class="learn-btn">Learn More</a>
</section>

<footer class="site-footer">
  <p class="copyright">Copyright © 2014, Zenvok, All Rights Reserved</p>
  <p class="footer-links">Are you a Property Manager?<span class="sep">|</span>About Us<span class="sep">|</span>Contact Us<span class="sep">|</span>Terms of Use<span class="sep">|</span>Privacy Policy<span class="sep">|</span>Site Map</p>
</footer>

</body>
</html>
```